Brisa Lumen Systems Corp Business Cards

Business cards to match the logo.

Company is a start up water technology company that has developed a patented system using centrifugal force to separate waste from municipal waste water to produce crystal clear clean water. Product sell starting at 2 million to governments both in the US and international.

Business cards should have a professional look with the target generally engineers.

Target Market(s)

Engineers, Government officials and investors

Industry/Entity Type

Water Treatment

Contact Information for Business Card

Business cards design will be used for 6 to 8 people with job titles. Can use the quote "If there is magic in the planet, it is contained in water." but not required to use quote. Should follow theme of Logo

Font styles to use
Other font styles liked:
• match logo font

Requirements
Nice to have
• Colors to match Logo. Business cards to match style of flow of Logo.
• Emphasis on clean look not a busy look. Clean flowing water.
Should not have
• Pictures of industrial equipment or wastewater

```html
<!DOCTYPE html>
<html lang="en">
<head>
<meta charset="utf-8">
<title>Brisa Lumen Systems Corp – Business Card</title>
<link rel="stylesheet" href="https://fonts.googleapis.com/css2?family=Lato:wght@400;700&display=swap">
<style>
  :root {
    --navy: #0c4a9e;
    --deep: #0a4fa8;
    --mid: #1f7fd0;
    --aqua: #4dd4fa;
    --ink: #141414;
    --paper: #ffffff;
  }
  html, body {
    margin: 0;
    padding: 0;
    width: 1200px;
    height: 719px;
    overflow: hidden;
    background: var(--paper);
  }
  .card {
    position: relative;
    width: 1200px;
    height: 719px;
    background: var(--paper);
    font-family: "Lato", Arial, sans-serif;
    color: var(--ink);
    overflow: hidden;
  }
  .footer-band {
    position: absolute;
    left: 0;
    right: 0;
    top: 584px;
    bottom: 0;
    background: radial-gradient(ellipse 640px 260px at 620px 100%, var(--aqua) 0%, var(--mid) 55%, var(--deep) 100%);
  }
  .brand-name {
    position: absolute;
    left: 126px;
    top: 180px;
    margin: 0;
    font-size: 54px;
    font-weight: 700;
    letter-spacing: 1px;
    line-height: 1;
    color: var(--navy);
    white-space: nowrap;
  }
  .address {
    position: absolute;
    left: 126px;
    top: 358px;
    margin: 0;
    font-style: normal;
    font-size: 27px;
    line-height: 37px;
  }
  .contact-list {
    position: absolute;
    left: 126px;
    top: 454px;
    margin: 0;
    padding: 0;
    list-style: none;
    font-size: 27px;
    line-height: 38px;
  }
  .contact-list li {
    display: flex;
    align-items: center;
    gap: 26px;
  }
  .contact-icon {
    width: 22px;
    height: 22px;
    flex: none;
  }
  .person {
    position: absolute;
    right: 131px;
    top: 362px;
    text-align: right;
  }
  .person-name {
    margin: 0;
    font-size: 41px;
    font-weight: 700;
    color: var(--aqua);
    line-height: 1.1;
  }
  .person-title {
    margin: 4px 0 0;
    font-size: 27px;
    font-weight: 400;
    line-height: 1.2;
  }
  .website {
    position: absolute;
    right: 131px;
    top: 604px;
    margin: 0;
    font-size: 26px;
    color: var(--paper);
  }
</style>
</head>
<body>
<main class="card">
  <div class="footer-band" role="img" aria-label="Flowing blue water wave decoration"></div>

  <h1 class="brand-name">BRISA LUMEN SYSTEMS</h1>

  <address class="address">
    418 Corran Lane<br>
    Austin, TX 78701
  </address>

  <ul class="contact-list">
    <li>
      <svg class="contact-icon" viewBox="0 0 22 22" aria-label="Mobile">
        <rect x="6" y="2" width="10" height="18" rx="2" fill="none" stroke="var(--aqua)" stroke-width="1.8"/>
        <circle cx="11" cy="17" r="1" fill="var(--aqua)"/>
      </svg>
      <span>555 010 4820</span>
    </li>
    <li>
      <svg class="contact-icon" viewBox="0 0 22 22" aria-label="Phone">
        <path fill="var(--aqua)" d="M5 2 L8.5 2 L10 7 L7.8 8.6 C9 11.2 10.8 13 13.4 14.2 L15 12 L20 13.5 L20 17 C20 18.7 18.6 20 17 20 C9 19.4 2.6 13 2 5 C2 3.4 3.3 2 5 2 Z"/>
      </svg>
      <span>555 010 4821</span>
    </li>
    <li>
      <svg class="contact-icon" viewBox="0 0 22 22" aria-label="Email">
        <rect x="1" y="5" width="20" height="13" fill="var(--aqua)"/>
        <path d="M1 5 L11 13 L21 5" fill="none" stroke="var(--paper)" stroke-width="1.6"/>
      </svg>
      <span>info@brisalumen.com</span>
    </li>
  </ul>

  <section class="person">
    <h2 class="person-name">Tomas Reyland</h2>
    <p class="person-title">Manager</p>
  </section>

  <p class="website">www.brisalumen.com</p>
</main>
</body>
</html>
```